Book Cover,

Our book is called "88 methods for wrecking your life but staying upright: Enduring Past University, Still one more Clichéd Diploma-era Coping Manual.
The Cover art for our book is very vivid in our minds and we hope YOU can help us bring it to life!

Picture a college graduation, cap, gown, cameras stadium the whole nine yards. now focus on one college graduate a guy, long black hair, diploma in his had, facing the crowd, his parents, flashes going off around him, behind him, is the exit of the graduation ceremony, where his class mates are exiting, but its not an exit, its the edge of a massive cliff, and students are falling down, you see people mid air falling down, at the bottom of the cliff is a trampoline, where the kids are bouncing off,

the idea and theory behind the art is the moral of the book, the book is a satire on all post college survival guides, (and god only knows how many horrible ones are out there). This is to make fun of them shed some light on the situation and really give good clear advice. so the art needs to be fun cartoonish feel and really scream satire.

Please dont hesitate to ask us for more direction, but we hope this is a great start!
Updates

Reason: We have not found something that we are set on please send us more submissions!

Reason: We have seen things we like but arent sold on any one yet- as well we have both been out of the country and have not had time to seriously consider all the submissions thank you

Target Market(s)

17-25

Industry/Entity Type

College

Requirements
Must have
• lots of colors, we want the art to be very vibrant, also a pencil look, we want the art to look like it was drawn onto the book
Should not have
• should not look digital it needs to have a real art feel to it.

```html
<!DOCTYPE html>
<html lang="en">
<head>
<meta charset="utf-8">
<title>88 Methods – Book Cover</title>
<link rel="stylesheet" href="https://fonts.googleapis.com/css2?family=Titan+One&family=Alfa+Slab+One&family=Tinos:wght@400;700&display=swap">
<style>
  :root {
    --stage: #ececec;
    --cover-blue: #173f92;
    --spine-blue: #12357f;
    --ink-navy: #141a2c;
    --paper: #ffffff;
    --body-text: #dfe6f5;
    --box-grey: #e4e4e4;
    --sky-top: #8fb5d6;
    --sky-mid: #d4e2ec;
    --city-low: #6d8496;
  }
  * { box-sizing: border-box; margin: 0; padding: 0; }
  html, body { width: 1200px; height: 800px; overflow: hidden; }
  body {
    background: var(--stage);
    display: flex; align-items: center; justify-content: center;
    font-family: "Tinos", serif;
  }
  .book-wrap { display: flex; height: 580px; box-shadow: 0 10px 30px rgba(0,0,0,.18); }

  /* Back cover */
  .back-cover {
    width: 370px; height: 100%;
    background: var(--cover-blue);
    padding: 20px 22px 26px;
    display: flex; flex-direction: column;
  }
  .back-author {
    font-family: "Alfa Slab One", serif; font-weight: 400; color: var(--ink-navy);
    font-size: 11px; margin-bottom: 4px;
  }
  .back-title {
    font-family: "Titan One", sans-serif; font-weight: 400; color: var(--ink-navy);
    font-size: 20px; line-height: 1.05; text-align: center;
    -webkit-text-stroke: 2px var(--paper); paint-order: stroke fill;
  }
  .back-subtitle {
    margin-top: 8px; text-align: center;
    font-family: "Alfa Slab One", serif; color: var(--ink-navy);
    -webkit-text-stroke: 1.5px var(--paper); paint-order: stroke fill;
  }
  .back-subtitle .main { font-size: 15px; display: block; }
  .back-subtitle .tag { font-size: 7.5px; display: block; }
  .blurb {
    margin-top: 16px; color: var(--body-text);
    font-size: 11px; line-height: 1.42; text-align: justify;
  }
  .back-footer { margin-top: auto; display: flex; justify-content: space-between; }
  .placeholder-box {
    width: 100px; height: 52px; background: var(--box-grey);
    display: flex; align-items: center; justify-content: center;
    font-weight: 700; font-size: 11px; color: #222;
  }

  /* Spine */
  .spine {
    width: 30px; height: 100%; background: var(--spine-blue);
    display: flex; align-items: center; justify-content: center;
    overflow: hidden; padding: 14px 0;
    border-left: 1px solid rgba(0,0,0,.25); border-right: 1px solid rgba(0,0,0,.25);
  }
  .spine-text {
    writing-mode: vertical-rl; white-space: nowrap;
    font-family: "Alfa Slab One", serif; font-size: 7.5px;
    color: var(--paper); letter-spacing: .2px;
    max-height: 100%; overflow: hidden;
  }
  .spine-text .spine-author { display: inline-block; margin-top: 40px; font-size: 7px; }

  /* Front cover */
  .front-cover { position: relative; width: 390px; height: 100%; overflow: hidden; }
  .cover-photo {
    position: absolute; inset: 0;
    background: linear-gradient(180deg, var(--sky-top) 0%, var(--sky-mid) 45%, #b9c6cf 60%, var(--city-low) 100%);
  }
  .front-author {
    position: absolute; top: 14px; right: 18px;
    font-family: "Alfa Slab One", serif; font-size: 13px; color: var(--ink-navy);
  }
  .front-title {
    position: absolute; right: 16px; top: 290px; width: 350px;
    font-family: "Titan One", sans-serif; font-weight: 400; color: var(--ink-navy);
    text-align: center; line-height: 1.02;
    -webkit-text-stroke: 3px var(--paper); paint-order: stroke fill;
  }
  .front-title span { display: block; white-space: nowrap; }
  .front-title .l1 { font-size: 34px; }
  .front-title .l2 { font-size: 34px; }
  .front-title .l3 { font-size: 34px; }
  .front-title .l4 { font-size: 42px; }
  .front-title .l5 { font-size: 46px; }
  .front-subtitle {
    position: absolute; right: 16px; bottom: 22px;
    background: var(--paper); padding: 2px 6px; text-align: center;
    font-family: "Alfa Slab One", serif; color: var(--ink-navy);
  }
  .front-subtitle .main { display: block; font-size: 14.5px; }
  .front-subtitle .tag { display: block; font-size: 7px; }
</style>
</head>
<body>
  <div class="book-wrap">
    <section class="back-cover">
      <div class="back-author">Author's Name</div>
      <h2 class="back-title">88 methods FOR WRECKING<br>YOUR LIFE BUT STAYING UPRIGHT</h2>
      <div class="back-subtitle">
        <span class="main">ENDURING PAST UNIVERSITY</span>
        <span class="tag">STILL ONE MORE CLICHÉD DIPLOMA-ERA COPING MANUAL</span>
      </div>
      <p class="blurb">Lorem ipsum dolor sit amet, consectetur adipisicing elit, sed do eiusmod tempor incididunt ut labore et dolore magna aliqua. Ut enim ad minim veniam, quis nostrud exercitation. Lorem ipsum dolor sit amet, consectetur adipisicing elit, sed do eiusmod tempor incididunt ut labore et dolore magna aliqua. Ut enim ad minim veniam, quis nostrud exercitation. Lorem ipsum dolor sit amet, consectetur adipisicing elit, sed do eiusmod tempor incididunt ut labore et dolore magna aliqua. Ut enim ad minim veniam, quis nostrud exercitation. Lorem ipsum dolor sit amet, consectetur adipisicing elit, sed do eiusmod tempor incididunt ut labore et dolore magna aliqua. Ut enim ad minim veniam, quis nostrud exercitation. Lorem ipsum dolor sit amet, consectetur adipisicing elit, sed do eiusmod tempor incididunt ut labore et dolore magna aliqua. Ut enim ad minim veniam, quis nostrud exercitation.</p>
      <div class="back-footer">
        <div class="placeholder-box">LOGO</div>
        <div class="placeholder-box">ISBN</div>
      </div>
    </section>

    <div class="spine">
      <div class="spine-text">88 METHODS FOR WRECKING YOUR LIFE BUT STAYING UPRIGHT<span class="spine-author">Author's Name</span></div>
    </div>

    <section class="front-cover">
      <div class="cover-photo" role="img" aria-label="Photo of a young man in a dark suit balancing on a tightrope cable high above a hazy city skyline under a blue sky"></div>
      <div class="front-author">Author's Name</div>
      <h1 class="front-title">
        <span class="l1">88 methods</span>
        <span class="l2">FOR WRECKING</span>
        <span class="l3">YOUR LIFE BUT</span>
        <span class="l4">STAYING</span>
        <span class="l5">UPRIGHT</span>
      </h1>
      <div class="front-subtitle">
        <span class="main">ENDURING PAST UNIVERSITY</span>
        <span class="tag">STILL ONE MORE CLICHÉD DIPLOMA-ERA COPING MANUAL</span>
      </div>
    </section>
  </div>
</body>
</html>
```